PowerPoint Design Project

We need a powerpoint design for our consulting company, Halvern Consulting. We provide technology strategy and solutioning services, with an emphasis on cloud technology. More information about our services can be found at www.halvernconsulting-example.com

We are looking for a design that is professional, but not corporate stuffy. The design needs to use our primary colors in our brand.
Updates

Reason: We need to iterate on some of the great designs, plus, many people have not had a chance to submit their design yet.

Reason: We had a lot of people accept the project, but not all of them have responded yet. We wanted to get them some time, plus, ask a couple of people to make some minor revisions.

Target Market(s)

Technology buyers between the ages of 30-55 at Pinnacle 900 companies

Industry/Entity Type

It Company

Requirements
Must have
• Must follow our logo colors.
Must have at least a cover slide and interior content slide.
Should not have
• Should not contain anything cartoonish or anything with lots of clouds

```html
<!DOCTYPE html>
<html lang="en">
<head>
<meta charset="utf-8">
<title>Halvern Consulting – Presentation Template</title>
<link rel="stylesheet" href="https://fonts.googleapis.com/css2?family=Arimo:ital,wght@0,400;0,700&display=swap">
<style>
  :root {
    --page-bg: #d4d4d4;
    --frame: #ffffff;
    --slide-edge: #c4c4c4;
    --slide-glow: #f4f4f4;
    --brand-teal: #13849c;
    --brand-teal-dark: #2f5d70;
    --text-dark: #2b2b2b;
    --text-white: #ffffff;
    --axis: #555555;
  }
  * { box-sizing: border-box; margin: 0; padding: 0; }
  html, body { width: 1200px; height: 1200px; overflow: hidden; }
  body {
    background: var(--page-bg);
    font-family: "Arimo", Arial, sans-serif;
  }
  .deck {
    position: relative;
    width: 1200px;
    height: 1200px;
  }
  .slide {
    position: absolute;
    width: 480px;
    height: 360px;
    border: 9px solid var(--frame);
    background: radial-gradient(ellipse at 55% 45%, var(--slide-glow) 0%, var(--slide-edge) 100%);
    box-shadow: 0 3px 10px rgba(0,0,0,0.25);
    overflow: hidden;
  }
  .slide--cover   { left: 100px; top: 20px; }
  .slide--text    { left: 620px; top: 20px; }
  .slide--bullets { left: 100px; top: 420px; }
  .slide--chart   { left: 620px; top: 420px; }
  .slide--closing { left: 360px; top: 820px; }

  .brand {
    position: absolute;
    left: 22px;
    top: 20px;
    display: flex;
    align-items: center;
    gap: 8px;
    color: var(--brand-teal);
    font-size: 19px;
    font-weight: 400;
  }
  .brand__dot {
    width: 16px; height: 16px;
    border-radius: 50%;
    background: var(--brand-teal);
  }

  .band {
    position: absolute;
    left: 0;
    right: 0;
    background: var(--brand-teal);
    color: var(--text-white);
    font-weight: 700;
    display: flex;
    align-items: center;
    justify-content: center;
    box-shadow: 0 3px 5px rgba(0,0,0,0.25);
  }
  .band--title {
    top: 34px;
    height: 50px;
    font-size: 26px;
  }
  .band--cover {
    top: 228px;
    height: 50px;
    font-size: 26px;
  }
  .band--closing {
    bottom: 0;
    height: 56px;
    font-size: 28px;
    letter-spacing: 0.5px;
  }
  .band__mark {
    position: absolute;
    left: 12px;
    top: 50%;
    transform: translateY(-50%);
    width: 36px; height: 36px;
    border-radius: 50%;
    background: var(--frame);
  }

  .body-copy {
    position: absolute;
    left: 34px;
    right: 30px;
    top: 108px;
    color: var(--text-dark);
    font-size: 15px;
    line-height: 1.45;
  }
  .bullet-list {
    position: absolute;
    left: 40px;
    right: 30px;
    top: 104px;
    list-style: none;
    color: var(--text-dark);
    font-size: 14px;
    line-height: 1.3;
  }
  .bullet-list li {
    position: relative;
    padding-left: 16px;
    margin-bottom: 6px;
  }
  .bullet-list li::before {
    content: "";
    position: absolute;
    left: 0; top: 6px;
    width: 7px; height: 7px;
    border-radius: 50%;
    background: var(--brand-teal);
  }
  .chart {
    position: absolute;
    left: 20px;
    top: 100px;
    width: 420px;
    height: 230px;
  }
  .chart text { font-family: "Arimo", Arial, sans-serif; fill: var(--axis); font-size: 10px; }
</style>
</head>
<body>
<main class="deck">

  <section class="slide slide--cover">
    <div class="brand"><span class="brand__dot"></span>Halvern Consulting</div>
    <h1 class="band band--cover">Title</h1>
  </section>

  <section class="slide slide--text">
    <h2 class="band band--title"><span class="band__mark"></span>Title</h2>
    <p class="body-copy">Lorem ipsum dolor sit amet, consectetur adipiscing elit. Nam et dolor scelerisque, condimentum sapien id, posuere justo. <strong>Interdum et malesuada</strong> fames ac ante ipsum primis in faucibus. Pellentesque vel auctor mi. Class aptent taciti sociosqu ad litora torquent per conubia nostra, per inceptos himenaeos.</p>
  </section>

  <section class="slide slide--bullets">
    <h2 class="band band--title"><span class="band__mark"></span>Title</h2>
    <ul class="bullet-list">
      <li>Lorem ipsum dolor sit amet, consectetur adipiscing elit.</li>
      <li>Nam et dolor scelerisque, condimentum sapien id, posuere justo.</li>
      <li><strong>Interdum et malesuada</strong> fames ac ante ipsum primis in faucibus.</li>
      <li>Pellentesque vel auctor mi.</li>
      <li>Class aptent taciti sociosqu ad litora torquent per conubia nostra, per inceptos himenaeos.</li>
    </ul>
  </section>

  <section class="slide slide--chart">
    <h2 class="band band--title"><span class="band__mark"></span>Title</h2>
    <svg class="chart" viewBox="0 0 420 230" role="img" aria-label="Bar chart comparing Region 1 and Region 2 from 2007 to 2010">
      <g stroke="#bbbbbb" stroke-width="1">
        <line x1="95" y1="10" x2="95" y2="200"/>
        <line x1="140" y1="10" x2="140" y2="200"/>
        <line x1="185" y1="10" x2="185" y2="200"/>
      </g>
      <line x1="50" y1="10" x2="50" y2="200" stroke="#888" stroke-width="1"/>
      <g>
        <rect x="50" y="18" width="22" height="14" fill="var(--brand-teal-dark)"/>
        <rect x="50" y="32" width="54" height="14" fill="var(--brand-teal)"/>
        <rect x="50" y="64" width="31" height="14" fill="var(--brand-teal-dark)"/>
        <rect x="50" y="78" width="59" height="14" fill="var(--brand-teal)"/>
        <rect x="50" y="110" width="77" height="14" fill="var(--brand-teal-dark)"/>
        <rect x="50" y="124" width="103" height="14" fill="var(--brand-teal)"/>
        <rect x="50" y="156" width="176" height="14" fill="var(--brand-teal-dark)"/>
        <rect x="50" y="170" width="108" height="14" fill="var(--brand-teal)"/>
      </g>
      <text x="42" y="35" text-anchor="end">2007</text>
      <text x="42" y="81" text-anchor="end">2008</text>
      <text x="42" y="127" text-anchor="end">2009</text>
      <text x="42" y="173" text-anchor="end">2010</text>
      <text x="50" y="216" text-anchor="middle">0</text>
      <text x="95" y="216" text-anchor="middle">25</text>
      <text x="140" y="216" text-anchor="middle">50</text>
      <text x="185" y="216" text-anchor="middle">75</text>
      <text x="230" y="216" text-anchor="middle">100</text>
      <rect x="262" y="20" width="9" height="9" fill="var(--brand-teal-dark)"/>
      <text x="278" y="28">Region 1</text>
      <rect x="332" y="20" width="9" height="9" fill="var(--brand-teal)"/>
      <text x="348" y="28">Region 2</text>
    </svg>
  </section>

  <section class="slide slide--closing">
    <h2 class="band band--closing">THANK YOU</h2>
  </section>

</main>
</body>
</html>
```